New design for our website – modern, elegant, and customer-focused

We want to redesign our website, www.tervalundex.se, to create a completely new look that reflects the high quality of our products and services. We are seeking assistance in developing a modern, clean, and user-friendly web experience in Flatsome that strengthens our brand and makes it easier for customers to find the right solutions. Our goal is to enhance the design, functionality, and overall impression to better meet today’s expectations and demands.

Target Market(s)

swimmingpool & spa

Industry/Entity Type

Poolbusiness

Coding

Coded - Design and coding required

Number of Pages Required

1 page

Font styles to use
Other font styles liked:
• HaboroSoft

Requirements
Must have
• We working in Flatsome
Nice to have
• From dream to reality – swimming pools that transform your garden into a place of life and enjoyment.
Should not have
• Nice look

```html
<!DOCTYPE html>
<html lang="en">
<head>
<meta charset="utf-8">
<title>Tervalundex – Premium Swimming Pools</title>
<link href="https://fonts.googleapis.com/css2?family=Montserrat:wght@600;700;800&family=Lato:wght@400;700&display=swap" rel="stylesheet">
<style>
:root{
  --navy:#1f4f8a;
  --navy-dark:#173f70;
  --sky:#e4f2fc;
  --sky-2:#f1f8fe;
  --footer:#3d9ee0;
  --text:#2b2f36;
  --muted:#6b7480;
  --line:#dbe3ea;
  --white:#ffffff;
  --pool:#2aa8d8;
}
*{box-sizing:border-box;margin:0;padding:0}
html,body{width:1200px;height:5352px;overflow:hidden}
body{font-family:"Lato",sans-serif;color:var(--text);background:var(--white);position:relative}
.h2{font-family:"Montserrat",sans-serif;font-weight:700;font-size:31px;color:var(--navy);text-align:center;letter-spacing:.5px;text-transform:uppercase}
.sub{font-size:11px;color:var(--muted);text-align:center;line-height:1.5}
.btn{display:inline-block;background:var(--navy);color:var(--white);font-size:12px;font-weight:700;padding:8px 18px;border-radius:2px;text-decoration:none}
.btn-center{position:absolute;left:50%;transform:translateX(-50%)}
.ph{display:block;border-radius:2px}
section,header,footer{position:absolute;left:0;width:1200px}
.more{font-size:10px;color:var(--navy);font-weight:700}
.bg{position:absolute;inset:0}
.layer{position:relative}

/* nav */
.nav{top:0;height:62px;display:flex;align-items:center;justify-content:space-between;padding:0 112px;background:var(--white)}
.brand{font-family:"Montserrat",sans-serif;font-weight:700;font-size:21px;color:var(--navy);display:flex;align-items:center;gap:8px}
.brand i{width:10px;height:10px;background:var(--navy);border-radius:50%}
.menu{display:flex;gap:34px;font-size:12px;font-weight:700;color:var(--navy);align-items:center}
.menu .btn{padding:6px 20px}

/* hero */
.hero{top:62px;height:562px;text-align:center;color:var(--white)}
.hero .bg{background:linear-gradient(180deg,#6fa9c9 0%,#3c8fb8 40%,#1d7fb4 70%,#1776ad 100%)}
.hero h1{font-family:"Montserrat",sans-serif;font-weight:800;font-size:56px;line-height:1.0;padding-top:205px}
.hero p{font-size:12px;font-weight:700;margin-top:16px;line-height:1.4}
.hero .ctas{margin-top:20px;display:flex;gap:12px;justify-content:center}
.btn-light{background:var(--white);color:var(--navy);border:1px solid var(--white)}

/* expertise */
.expertise{top:672px}
.exp-cards{position:absolute;top:70px;left:112px;display:flex;gap:18px}
.exp-card{width:231px;height:230px;position:relative;border-radius:2px;overflow:hidden}
.exp-card .cap{position:absolute;left:12px;right:12px;bottom:14px;color:var(--white);font-family:"Montserrat",sans-serif;font-weight:700;font-size:13px;display:flex;justify-content:space-between;align-items:flex-end}
.exp-card small{display:block;font-family:"Lato",sans-serif;font-weight:400;font-size:9px;margin-top:3px;line-height:1.3}

/* why */
.why{top:1037px;height:353px}
.why-img{position:absolute;left:112px;top:0;width:399px;height:353px}
.why-body{position:absolute;left:553px;top:6px;width:486px}
.why-body .h2{text-align:left;font-size:29px}
.why-body .sub{text-align:left;margin-top:8px}
.why-rows{margin-top:16px;display:flex;flex-direction:column;gap:13px}
.why-row{height:46px;background:var(--sky);display:flex;align-items:center;padding:0 12px;gap:12px;border-radius:2px}
.why-row .ic{width:22px;height:22px;border:1.5px solid var(--navy);border-radius:50%;flex:none}
.why-row .t{flex:1;font-size:10px;color:var(--muted);line-height:1.4}
.why-row .t b{color:var(--navy);font-size:10.5px;display:block}

/* services */
.services{top:1446px}
.srv-cards{position:absolute;top:79px;left:112px;display:flex;gap:19px}
.srv-card{width:312px;height:339px;border:1px solid var(--line);background:var(--white)}
.srv-card .ph{height:218px;border-radius:0}
.srv-card .b{padding:14px 13px}
.srv-card h3{font-family:"Montserrat",sans-serif;font-size:13px;color:var(--text);font-weight:700}
.srv-card p{font-size:9.5px;color:var(--muted);margin:7px 0 6px;line-height:1.5}

/* about */
.about{top:1974px;height:395px;background:var(--sky)}
.about .txt{position:absolute;left:112px;top:88px;width:430px}
.about .h2{text-align:left}
.about p{font-size:10px;color:var(--muted);line-height:1.5;margin-top:10px}
.about .btn{margin-top:12px}
.about .ph{position:absolute;left:611px;top:52px;width:476px;height:291px}

/* accessories */
.acc{top:2412px;height:310px}
.acc-cards{position:absolute;top:71px;left:112px;display:flex;gap:18px}
.acc-card{width:230px;height:233px;background:var(--sky-2)}
.acc-card .prod{height:200px;background:linear-gradient(180deg,#f1f8fe,#dfeaf3)}
.acc-card .lbl{height:33px;background:var(--navy);color:var(--white);font-size:12px;font-weight:700;display:flex;align-items:center;padding-left:12px}
.arrow{position:absolute;width:30px;height:30px;border:1px solid var(--navy);background:var(--white);display:flex;align-items:center;justify-content:center}

/* gallery */
.gallery{top:2762px}
.gallery .sub{margin-top:10px}

/* testimonials */
.testi{top:3572px}
.t-cards{position:absolute;top:71px;left:112px;display:flex;gap:19px}
.t-card{width:312px;height:201px;background:var(--sky-2);text-align:center;padding-top:18px}
.avatar{width:38px;height:38px;border-radius:50%;background:linear-gradient(#9bb3c9,#5f7e9b);margin:0 auto}
.stars{color:#f3b400;font-size:9px;margin-top:6px;letter-spacing:1px}
.t-card p{font-size:9.5px;color:var(--muted);line-height:1.45;margin:6px 30px 0}
.t-card b{display:block;font-size:10px;margin-top:8px}
.t-card small{font-size:9px;color:#a0a7ae}

/* experience band */
.exp-band{top:3902px;height:192px;text-align:center;color:var(--white)}
.exp-band .bg{background:linear-gradient(180deg,#2a6fa6,#1c5b92)}
.exp-band h2{font-family:"Montserrat",sans-serif;font-weight:700;font-size:31px;padding-top:44px}
.exp-band p{font-size:10px;margin:4px auto 0;width:660px;line-height:1.4}
.exp-band .btn{margin-top:16px;background:var(--white);color:var(--navy)}

/* blog */
.blog{top:4137px}
.b-cards{position:absolute;top:71px;left:112px;display:flex;gap:19px}
.b-card{width:312px}
.b-card .ph{height:200px}
.b-card .date{font-size:10px;color:#5aa3d8;margin-top:14px;display:flex;align-items:center;gap:6px}
.b-card .date i{width:12px;height:12px;border:1.5px solid #5aa3d8;border-radius:2px}
.b-card h3{font-family:"Montserrat",sans-serif;font-size:12px;font-weight:700;margin-top:8px}
.b-card p{font-size:9.5px;color:var(--muted);line-height:1.45;margin:6px 0}

/* contact */
.contact{top:4624px;height:453px}
.contact .bg{background:linear-gradient(180deg,#2e7fb5,#14608f)}
.contact .map{position:absolute;left:112px;top:62px;width:478px;height:328px;background:#eef1f3}
.contact h2{position:absolute;left:675px;top:90px;font-family:"Montserrat",sans-serif;font-size:31px;font-weight:700;color:var(--white)}
.field{position:absolute;border:1.5px solid var(--white);color:var(--white);font-size:10px;padding:7px 10px;border-radius:2px}

/* footer */
.footer{top:5077px;height:275px;background:var(--footer);color:var(--white)}
.footer .col{position:absolute;top:44px;font-size:10px;line-height:1.75}
.footer h4{font-family:"Montserrat",sans-serif;font-size:15px;font-weight:700;margin-bottom:14px;margin-top:16px}
.social{display:flex;gap:10px;margin-top:12px}
.social i{width:22px;height:22px;border-radius:50%;background:var(--white)}
.copy{position:absolute;bottom:0;left:0;width:1200px;height:36px;border-top:1px solid rgba(255,255,255,.4);font-size:10px;display:flex;align-items:center;justify-content:center}
</style>
</head>
<body>

<header class="nav">
  <div class="brand"><i></i>Tervalundex</div>
  <nav class="menu">
    <span>Home</span><span>Services</span><span>About Us</span><span>Products</span><span>Pools</span><span>Gallery</span><span>Contact</span>
    <span class="btn">Login</span>
  </nav>
</header>

<section class="hero">
  <div class="bg" role="img" aria-label="Resort swimming pool with palm trees and parasols under a blue sky"></div>
  <div class="layer">
    <h1>Turning Visions into Pools<br>of Perfection</h1>
    <p>We create premium swimming pools that combine Scandinavian design, modern technology,<br>and exceptional craftsmanship</p>
    <div class="ctas"><span class="btn">Get A Quote</span><span class="btn btn-light">Explore Our Pools</span></div>
  </div>
</section>

<section class="expertise">
  <h2 class="h2">Our Expertise</h2>
  <div class="exp-cards">
    <div class="exp-card" role="img" aria-label="Infinity pool facing the sea with palm trees" style="background:linear-gradient(180deg,#4a9ac8,#1b6ea3 60%,#0b2a3f)">
      <div class="cap"><div>Swimming Pools<small>Custom-built pools designed for<br>your home and climate</small><small style="font-weight:700">Learn More →</small></div></div>
    </div>
    <div class="exp-card" role="img" aria-label="Person relaxing in a spa setting" style="background:linear-gradient(180deg,#b6a58e,#e8e3dc 50%,#3b3a38)">
      <div class="cap"><span>Spas And Wellness</span><span>›</span></div>
    </div>
    <div class="exp-card" role="img" aria-label="Technician servicing pool equipment" style="background:linear-gradient(180deg,#7b8d83,#4c5a50 50%,#1f2622)">
      <div class="cap"><span>Pool Maintenance</span><span>›</span></div>
    </div>
    <div class="exp-card" role="img" aria-label="Pool accessories by the water's edge" style="background:linear-gradient(180deg,#5fc1e4,#3aa4d1 50%,#a36f3d)">
      <div class="cap"><span>Pool Accessories &amp;<br>Equipments</span><span>›</span></div>
    </div>
  </div>
</section>

<section class="why">
  <div class="why-img ph" role="img" aria-label="Woman relaxing in a sunny swimming pool" style="background:linear-gradient(160deg,#2aa4a0,#2cb3c9 50%,#1a86b8)"></div>
  <div class="why-body">
    <h2 class="h2">Why Choose Us</h2>
    <p class="sub">We combine craftsmanship, innovation, and care to deliver pools that are beautiful, durable,<br>and uniquely yours. From design to maintenance, we make your pool journey smooth,<br>professional, and stress-free.</p>
    <div class="why-rows">
      <div class="why-row"><i class="ic"></i><div class="t"><b>Expert Knowledge</b>Decades of experience in pool design, construction, and water systems</div><span>→</span></div>
      <div class="why-row"><i class="ic"></i><div class="t"><b>Premium Materials</b>We use only high-quality, durable, and eco-friendly materials for result</div><span>→</span></div>
      <div class="why-row"><i class="ic"></i><div class="t"><b>Trusted by Homeowners</b>A reputation built on reliability, excellence, and long-term client</div><span>→</span></div>
      <div class="why-row"><i class="ic"></i><div class="t"><b>Sustainability Focus</b>Built for beauty, designed for sustainability</div><span>→</span></div>
    </div>
  </div>
</section>

<section class="services">
  <h2 class="h2">Our Pool Services</h2>
  <p class="sub" style="margin-top:8px">We design and build custom swimming pools that combine beauty, performance, and lasting quality — tailored perfectly to your space and lifestyle</p>
  <div class="srv-cards">
    <div class="srv-card"><div class="ph" role="img" aria-label="Composite fiberglass pool with garden" style="background:linear-gradient(180deg,#7fae7e,#47b7d6 55%,#2798c8)"></div>
      <div class="b"><h3>Composite Fiberglass Pool</h3><p>Experience the perfect balance of luxury and practicality with our composite fiberglass pools. Designed for modern living, they're easy to...</p><span class="more">Learn More →</span></div></div>
    <div class="srv-card"><div class="ph" role="img" aria-label="Linear pool with sun loungers" style="background:linear-gradient(180deg,#c45a5a,#8a8f95 40%,#4fc1e3)"></div>
      <div class="b"><h3>Linear Pool</h3><p>Our liner pools offer a perfect blend of flexibility, comfort, and style. Designed for easy maintenance and quick installation, they deliver lasting...</p><span class="more">Learn More →</span></div></div>
    <div class="srv-card"><div class="ph" role="img" aria-label="Designer pool beside a building" style="background:linear-gradient(180deg,#a9c9e0,#b0693f 45%,#2aa8d8)"></div>
      <div class="b"><h3>Veldra Pool</h3><p>Veldra pools combine the sleek aesthetics of a designer pool with the precision of modern engineering. Each pool is custom-built...</p><span class="more">Learn More →</span></div></div>
  </div>
  <span class="btn btn-center" style="top:437px">View All</span>
</section>

<section class="about">
  <div class="txt">
    <h2 class="h2">About Us</h2>
    <p>At Tervalundex, we specialize in creating high-quality swimming pools and spas that combine modern design, advanced technology, and Scandinavian craftsmanship. With a focus on precision, sustainability, and customer satisfaction, we turn your vision into a pool built to inspire and last</p>
    <p style="margin-top:4px">Tervalundex transforms outdoor spaces into places of beauty, relaxation, and connection. Our team takes pride in delivering complete, worry-free solutions — from planning and design to installation and ongoing service</p>
    <span class="btn">Learn More</span>
  </div>
  <div class="ph" role="img" aria-label="Tropical pool surrounded by palm trees" style="background:linear-gradient(180deg,#5b8f3e,#6aa246 45%,#2cb4d5)"></div>
</section>

<section class="acc">
  <h2 class="h2">Our Pool Accessories</h2>
  <div class="arrow" style="left:67px;top:147px"><svg width="10" height="10" viewBox="0 0 10 10"><path d="M7 1 3 5l4 4" fill="none" stroke="#1f4f8a" stroke-width="1.5"/></svg></div>
  <div class="arrow" style="left:1100px;top:147px"><svg width="10" height="10" viewBox="0 0 10 10"><path d="M3 1l4 4-4 4" fill="none" stroke="#1f4f8a" stroke-width="1.5"/></svg></div>
  <div class="acc-cards">
    <div class="acc-card"><div class="prod" role="img" aria-label="Product photo of a robotic pool cleaner"></div><div class="lbl">Pool Robot →</div></div>
    <div class="acc-card"><div class="prod" role="img" aria-label="Product photo of a UV purification unit"></div><div class="lbl">UV Purification →</div></div>
    <div class="acc-card"><div class="prod" role="img" aria-label="Product photo of a pool heat exchanger"></div><div class="lbl">Heat Exchanger →</div></div>
    <div class="acc-card"><div class="prod" role="img" aria-label="Product photo of a sand filter tank"></div><div class="lbl">Sandfilter →</div></div>
  </div>
</section>

<section class="gallery">
  <h2 class="h2">Our Gallery</h2>
  <p class="sub">Explore our gallery to see how we transform outdoor spaces into stunning pool environments<br>that blend design, quality, and relaxation</p>
  <div class="ph" role="img" aria-label="Pool with wooden deck beside trees and sea" style="position:absolute;left:112px;top:101px;width:644px;height:296px;background:linear-gradient(160deg,#7e9aa6,#4b6f46 35%,#28b7df 70%,#5b4a3a)"></div>
  <div class="ph" role="img" aria-label="Resort pool with loungers and palms" style="position:absolute;left:775px;top:101px;width:312px;height:296px;background:linear-gradient(180deg,#a9c8d8,#4e8f63 40%,#2299d0)"></div>
  <div class="ph" role="img" aria-label="Curved tropical pool with greenery" style="position:absolute;left:112px;top:417px;width:314px;height:298px;background:linear-gradient(180deg,#3f6b35,#2f7c6a 50%,#1a8cbf)"></div>
  <div class="ph" role="img" aria-label="Large hotel pool in front of a building" style="position:absolute;left:445px;top:417px;width:642px;height:298px;background:linear-gradient(180deg,#6aa15a,#c9b79a 30%,#25a5dc 65%,#e0c15a)"></div>
  <span class="btn btn-center" style="top:740px">View All</span>
</section>

<section class="testi">
  <h2 class="h2">What Our Clients Say</h2>
  <div class="arrow" style="left:67px;top:155px"><svg width="10" height="10" viewBox="0 0 10 10"><path d="M7 1 3 5l4 4" fill="none" stroke="#1f4f8a" stroke-width="1.5"/></svg></div>
  <div class="arrow" style="left:1100px;top:155px"><svg width="10" height="10" viewBox="0 0 10 10"><path d="M3 1l4 4-4 4" fill="none" stroke="#1f4f8a" stroke-width="1.5"/></svg></div>
  <div class="t-cards">
    <div class="t-card"><div class="avatar" role="img" aria-label="Client portrait"></div><div class="stars">★★★★★</div><p>From the first meeting to the final handover, everything was handled with precision and care. We couldn't be happier with the quality and design of our pool</p><b>Oskar L.</b><small>Businessman</small></div>
    <div class="t-card"><div class="avatar" role="img" aria-label="Client portrait"></div><div class="stars">★★★★★</div><p>The team at Tervalundex exceeded our expectations in every way. They guided us through each step with clarity and delivered a pool that looks stunning and performs flawlessly</p><b>Lina K.</b><small>Designer</small></div>
    <div class="t-card"><div class="avatar" role="img" aria-label="Client portrait"></div><div class="stars">★★★★★</div><p>From start to finish, everything was handled with professionalism and care. The final result is a pool that's both elegant and easy to maintain — exactly what we wanted</p><b>Peter S.</b><small>Businessman</small></div>
  </div>
</section>

<section class="exp-band">
  <div class="bg" role="img" aria-label="Pool water background"></div>
  <div class="layer">
    <h2>OVER 25 YEARS OF EXPERIENCE</h2>
    <p>At Tervalundex, we bring decades of experience in designing and installing premium swimming pools and spas. We focus on Scandinavian quality, aesthetics, and sustainable solutions that enhance your home and lifestyle</p>
    <span class="btn">Learn More</span>
  </div>
</section>

<section class="blog">
  <h2 class="h2">Latest Blog</h2>
  <div class="b-cards">
    <div class="b-card"><div class="ph" role="img" aria-label="Poolside parasols and loungers" style="background:linear-gradient(180deg,#e8efe9,#7fb07a 40%,#39b6d9)"></div><div class="date"><i></i>16 September, 2025</div><h3>Choosing the Right Pool for Your Home</h3><p>Discover the key differences between composite, liner, and VELDRA pools — and how to...</p><span class="more">Learn More →</span></div>
    <div class="b-card"><div class="ph" role="img" aria-label="Clear blue pool with loungers" style="background:linear-gradient(180deg,#6ab0e0,#3e8d5a 35%,#1fa3d9)"></div><div class="date"><i></i>17 September, 2025</div><h3>Keep Your Pool Crystal Clear</h3><p>Simple maintenance tips to keep your water sparkling all year round...</p><span class="more">Learn More →</span></div>
    <div class="b-card"><div class="ph" role="img" aria-label="Lagoon style pool among trees" style="background:linear-gradient(180deg,#3f7d3a,#35a06a 45%,#20b5c3)"></div><div class="date"><i></i>18 September, 2025</div><h3>Eco-Friendly Pool Ideas</h3><p>Learn how to save energy and water with smart, sustainable pool systems...</p><span class="more">Learn More →</span></div>
  </div>
  <span class="btn btn-center" style="top:410px">View All</span>
</section>

<section class="contact">
  <div class="bg" role="img" aria-label="Pool at dusk background"></div>
  <div class="map" role="img" aria-label="Street map showing the office location"></div>
  <h2>CONTACT US</h2>
  <div class="field" style="left:675px;top:152px;width:412px">Your Name</div>
  <div class="field" style="left:675px;top:200px;width:200px">Email</div>
  <div class="field" style="left:887px;top:200px;width:200px">Mobile No.</div>
  <div class="field" style="left:675px;top:248px;width:412px;height:66px">Message...</div>
  <span class="btn" style="position:absolute;left:675px;top:330px;background:var(--white);color:var(--navy);padding:6px 26px">Send</span>
</section>

<footer class="footer">
  <div class="col" style="left:112px;width:260px;top:40px">
    <div class="brand" style="color:var(--white)"><i style="background:var(--white)"></i>Tervalundex</div>
    <div style="margin-top:10px">559000-1234</div>
    <div>Tervalundex creates high-quality, modern swimming pools designed for beauty, comfort, and long-lasting enjoyment</div>
    <div class="social"><i></i><i></i><i></i><i></i></div>
  </div>
  <div class="col" style="left:417px"><h4>QUICK LINKS</h4>Home<br>About Us<br>Services<br>Products<br>Gallery<br>Blog</div>
  <div class="col" style="left:628px"><h4>SERVICES</h4>Swimming Pools<br>Spas &amp; Wellness<br>Pool Maintenance<br>Pool Equipments<br>Hot Tub<br>Pool Accessories</div>
  <div class="col" style="left:825px"><h4>CONTACT</h4>
    <div style="display:flex;gap:8px"><svg width="10" height="14" viewBox="0 0 10 14"><path d="M5 13S1 8 1 5a4 4 0 0 1 8 0c0 3-4 8-4 8z" fill="none" stroke="#fff"/><circle cx="5" cy="5" r="1.4" fill="#fff"/></svg><span>Strandvägen 14<br>392 30 Norrvik<br>Sweden</span></div>
    <div style="display:flex;gap:8px;margin-top:6px"><svg width="12" height="12" viewBox="0 0 12 12"><path d="M2 1h3l1 3-2 1a7 7 0 0 0 3 3l1-2 3 1v3c-6 0-9-3-9-9z" fill="none" stroke="#fff"/></svg>010 555 02 48</div>
    <div style="display:flex;gap:8px;margin-top:6px"><svg width="12" height="10" viewBox="0 0 12 10"><rect x=".5" y=".5" width="11" height="9" fill="none" stroke="#fff"/><path d="M1 1l5 4 5-4" fill="none" stroke="#fff"/></svg>kontakt@tervalundex.se</div>
  </div>
  <div class="copy">Copyright 2025 © Tervalundex</div>
</footer>

</body>
</html>
```